Uncoded front page web design for wedding and event planning company

Hi.

I am launching a wedding and event planning company called Silver Fern Gatherings and need a professional and appealing web design.

So, let me explain my company. I am based in Swindon in Wiltshire but the company will plan weddings and events in Oxfordshire, Wiltshire, Berkshire and London.

We will plan weddings, birthdays, conferences, product launches, fashion shows and conventions but the main focus of the website at this stage should be the weddings with all the other occasions being covered under a single 'events' heading.

My contact details for the website should be:
Maureen Pollard
maureen@silverferngatherings.co.uk
01632 960571 / 07700 900384

I'd like the website to feel clean, bright and elegant and be set against a white or off-white background. My logo is purple and I'd therefore like some purple incorporated into the design although feel free to use a more muted purple as my one might be a little bright? I'm also considering whether it would look nice paired with a little of the colour gold - maybe as a font colour in places?? I'll leave you to figure that one out as your design eye will be better than mine but for your reference below is my purple colour and my suggested gold one....

My purple colour is Pantone 2592 C but feel free to use others
My suggested gold I'm looking at is Pantone 14-1041 TCX

I would like to incorporate a Friendwall feed in the front page if possible, if it looks right. I'd also like to include a variety of pictures as well so I've included a few in a Dropbox folder which is linked below. Please don't feel obliged to use them all by any means (there's loads!) but you've got a few there to play with. If you find any other royalty free images you'd rather use please go ahead but on the understanding I can have them afterwards!

My logo can be retrieved via this Dropbox link...
You'll notice there are 2 styles of placement. Please feel free to use either to fit in with your design...
https://www.filebarrow.net/sh/kq7pw2mzt4xn8bc/BBBLqr5hoPnvtc6S41MkwvaHb?dl=0

The wedding images I have are in this Dropbox folder...
https://www.filebarrow.net/sh/r8ym3vk6fa2lp9q/BBB4dzrTy8kW5nh63LxPeqjsc?dl=0

Other than that, it's over to you.... I can't wait to receive your designs :-)

Ooh....finally just to say, as I receive designs in I think I'll notice aspects that I like and don't like and if I feel they'll be useful for other designers, I'll update my brief below. Thanks

BRIEF UPDATE:
Someone asked if I had a tag-line. Could you use "Creating exquisite occasions today for amazing memories tomorrow"

I realise I hadn't explained what I'd like included on my home page so here's some notes to consider....

A welcome to section for me to start narrative about us and our services which has a button that links to our 'about us' page and 'services' page for further information.

A section that nicely illustrates what services we offer whether that be with icons or pictures.

A section with some photos in that would link to our gallery

A section that shows some customer reviews and blog entries that would link to my reviews page and blog to read more.

And finally a contact us section with my details, social media links and site map.

***
I also need to draw attention to where in the UK my services cover. I was therefore thinking perhaps we could use a picture to demonstrate this where it highlights Wiltshire, Oxfordshire, Berkshire and London on a map thereby demonstrating our areas covered. I have found several English county maps when searching on Google but I'm not sure how to highlight the areas I cover (or dull out the areas I don't) so if you have any ideas on this, I'd really like it incorporated. Thanks. (by the way, for those of you not familiar with English counties, the ones I cover are often abbreviated to Wilts, Oxon, Berks, London, so if you find a suitable map with those names on rather than the full names, you'll know what they are!)

I've found an image of the county map which might work well. I was wondering whether we might somehow grey out the counties I don't cover and just keep the ones I do as mentioned above and then crop it into perhaps a shadowed circle? I've attached a screenshot to the brief.
Updates

I've decided on the tag-line "Creating exquisite occasions today for amazing memories tomorrow" so if that could be included somewhere that would be great. I also need to draw attention to where in the UK my services cover. I was therefore thinking perhaps we could use a picture to demonstrate this where it highlights Wiltshire, Oxfordshire, Berkshire and London on a map thereby demonstrating our areas covered. I have found several English county maps when searching on Google but I'm not sure how to highlight the areas I cover (or dull out the areas I don't) so if you have any ideas on this, I'd really like it incorporated. Thanks. Added Wednesday, June 24, 2015

Target Market(s)

Predominately women aged 25-55

Industry/Entity Type

Wedding Planner

Number of Pages Required

1 page

Font styles to use
Sans Serif
Script

Requirements
Nice to have
• I'd like to see how the colour theme of purple and perhaps a little gold (maybe as a font colour) look against a white background. I've mentioned the Pantone colours in the brief above.
• I've attached a screenshot of a webpage with gold writing in and fonts that I like. Perhaps it could give you inspiration?
Should not have
• I really don't like the font SCRIPTINA so please done use that.

```html
<!DOCTYPE html>
<html lang="en">
<head>
<meta charset="utf-8">
<title>Silver Fern Gatherings</title>
<link href="https://fonts.googleapis.com/css2?family=Open+Sans:wght@400;600;700&family=Cormorant+Garamond:wght@600&family=Arimo:wght@400;700&display=swap" rel="stylesheet">
<style>
  :root {
    --purple: #6b2579;
    --gold: #c8892e;
    --gold-dark: #b37a26;
    --gold-mid: #c0832b;
    --ink: #333333;
    --muted: #666666;
    --topbar: #3a3a3a;
    --footer: #353535;
    --footer-base: #262626;
    --footer-text: #bdbdbd;
    --white: #ffffff;
    --rule: #e4e4e4;
  }
  * { margin: 0; padding: 0; box-sizing: border-box; }
  html, body { width: 750px; height: 1200px; overflow: hidden; background: var(--white); }
  body { position: relative; font-family: "Open Sans", sans-serif; color: var(--ink); }
  .abs { position: absolute; }

  /* top bar */
  .topbar { left: 0; top: 0; width: 750px; height: 18px; background: var(--topbar); color: var(--white); font-size: 7.5px; }
  .topbar-item { position: absolute; top: 4px; display: flex; align-items: center; gap: 4px; }
  .topbar-item svg { width: 8px; height: 8px; fill: var(--white); }

  /* header */
  .header { left: 0; top: 18px; width: 750px; height: 58px; background: var(--white); }
  .brand { position: absolute; left: 62px; top: 12px; display: flex; align-items: center; gap: 5px; }
  .brand-dot { width: 14px; height: 14px; border-radius: 50%; background: var(--purple); }
  .brand-name { color: var(--purple); font-size: 10px; font-weight: 600; line-height: 12px; }
  .nav { position: absolute; top: 25px; display: flex; font-size: 8.5px; color: #555; }
  .nav a { position: absolute; color: #555; text-decoration: none; white-space: nowrap; }

  /* hero */
  .hero { left: 0; top: 76px; width: 750px; height: 286px;
    background: radial-gradient(ellipse at 52% 35%, #cdbfb3 0%, #8d7a6f 25%, #4d3a36 55%, #2c2226 100%); }
  .hero-title { position: absolute; left: 60px; top: 100px; color: var(--white);
    font-family: "Cormorant Garamond", serif; font-weight: 600; font-size: 17px; line-height: 20px; text-transform: uppercase; letter-spacing: 0.3px; }
  .hero-arrow { position: absolute; top: 132px; width: 20px; height: 20px; border-radius: 50%; background: rgba(40,40,40,0.55); }
  .hero-arrow svg { width: 20px; height: 20px; stroke: rgba(255,255,255,0.8); fill: none; stroke-width: 2; }

  /* services */
  .services { left: 62px; top: 310px; width: 627px; height: 91px; display: flex; box-shadow: 0 14px 14px -10px rgba(0,0,0,0.35); }
  .service { flex: 1; position: relative; color: var(--white); }
  .service:nth-child(1) { background: var(--gold-dark); }
  .service:nth-child(2) { background: var(--gold-mid); }
  .service:nth-child(3) { background: var(--gold); }
  .service-icon { position: absolute; left: 13px; top: 16px; width: 34px; height: 34px; stroke: var(--white); fill: none; stroke-width: 2.2; }
  .service-title { position: absolute; left: 56px; top: 17px; font-size: 10px; font-weight: 700; letter-spacing: 0.2px; }
  .service-text { position: absolute; left: 56px; top: 35px; width: 142px; font-size: 6.6px; line-height: 13.4px; }

  /* welcome */
  .section-title { left: 0; width: 750px; text-align: center; color: var(--purple); font-size: 13px; font-weight: 700; letter-spacing: 0.2px; }
  .welcome-text { left: 105px; top: 464px; width: 540px; text-align: center; color: var(--muted); font-size: 9px; line-height: 15.5px; }
  .divider { left: 136px; top: 531px; width: 478px; height: 1px; background: linear-gradient(to right, transparent, var(--rule) 15%, var(--rule) 85%, transparent); }
  .events-sub { left: 0; top: 573px; width: 750px; text-align: center; color: var(--muted); font-size: 9px; }

  /* events grid */
  .event { position: absolute; width: 145px; }
  .event-photo { width: 145px; height: 102px; }
  .event-title { margin-top: 11px; font-size: 7.3px; font-weight: 700; color: var(--ink); text-transform: uppercase; }
  .event-date { margin-top: 3px; font-size: 6.8px; color: var(--muted); }
  .btn-more { left: 326px; top: 918px; width: 98px; height: 27px; background: var(--gold); color: var(--white);
    font-size: 7px; text-transform: uppercase; display: flex; align-items: center; justify-content: center; box-shadow: 0 1px 2px rgba(0,0,0,0.2); }

  /* footer */
  .footer { left: 0; top: 986px; width: 750px; height: 182px; background: var(--footer); }
  .footer-base { left: 0; top: 1168px; width: 750px; height: 32px; background: var(--footer-base); color: var(--footer-text); font-size: 7px; text-align: center; line-height: 32px; }
  .footer-heading { position: absolute; color: var(--white); font-size: 7.5px; font-weight: 700; text-transform: uppercase; }
  .feed { position: absolute; left: 78px; font-family: "Arimo", sans-serif; }
  .feed-text { font-size: 6.2px; color: #9a9a9a; }
  .feed-link { margin-top: 5px; font-size: 6.6px; font-weight: 700; color: var(--white); }
  .feed-nav { position: absolute; left: 233px; top: 1013px; font-size: 8px; color: #aaa; letter-spacing: 3px; }
  .footer-links { position: absolute; list-style: none; font-size: 7.2px; color: var(--footer-text); line-height: 14px; }
  .social { position: absolute; left: 595px; display: flex; align-items: center; gap: 5px; font-size: 7.2px; color: var(--footer-text); }
  .social-dot { width: 17px; height: 17px; border-radius: 50%; background: #5a5a5a; }
</style>
</head>
<body>

<div class="abs topbar">
  <div class="topbar-item" style="left:62px">
    <svg viewBox="0 0 10 10"><path d="M2 0.5 L3.8 0.5 L4.4 2.8 L3.2 3.8 Q4.2 5.8 6.2 6.8 L7.2 5.6 L9.5 6.2 L9.5 8 Q9.5 9.5 8 9.5 Q0.5 9 0.5 2 Q0.5 0.5 2 0.5 Z"/></svg>
    <span>Call Us : 01632 960571 / 07700 900384</span>
  </div>
  <div class="topbar-item" style="left:259px">
    <svg viewBox="0 0 10 10"><path d="M0.5 2 L9.5 2 L9.5 8.5 L0.5 8.5 Z M0.5 2 L5 5.5 L9.5 2" stroke="#3a3a3a" stroke-width="0.8"/></svg>
    <span>Email Us : maureen@silverferngatherings.co.uk</span>
  </div>
  <div class="topbar-item" style="left:475px">
    <svg viewBox="0 0 10 10"><path d="M5 0.5 Q8.5 0.5 8.5 4 Q8.5 6 5 9.8 Q1.5 6 1.5 4 Q1.5 0.5 5 0.5 Z"/></svg>
    <span>Address : 120 STreet name, city name, Country name : 3652233</span>
  </div>
</div>

<header class="abs header">
  <div class="brand">
    <span class="brand-dot"></span>
    <span class="brand-name">Silver Fern<br>Gatherings</span>
  </div>
  <nav class="nav">
    <a style="left:371px">Home</a>
    <a style="left:437px">Weddings</a>
    <a style="left:518px">Events</a>
    <a style="left:587px">Gallery</a>
    <a style="left:657px">Contact</a>
  </nav>
</header>

<section class="abs hero" role="img" aria-label="Bride and groom dancing under falling confetti at a wedding reception">
  <h1 class="hero-title">We are wedding and<br>event planning company</h1>
  <div class="hero-arrow" style="left:24px"><svg viewBox="0 0 20 20"><path d="M12 5 L7 10 L12 15"/></svg></div>
  <div class="hero-arrow" style="left:706px"><svg viewBox="0 0 20 20"><path d="M8 5 L13 10 L8 15"/></svg></div>
</section>

<section class="abs services">
  <div class="service">
    <svg class="service-icon" viewBox="0 0 34 34"><circle cx="12" cy="21" r="9"/><circle cx="22" cy="21" r="9"/><path d="M9 8 L12 4 L15 8 L12 11 Z" stroke-width="1.6"/></svg>
    <div class="service-title">WEDDINGS</div>
    <div class="service-text">Lorem Ipsum is simply dummy text of the printing and typesetting industry printing and typesetting industry...</div>
  </div>
  <div class="service">
    <svg class="service-icon" viewBox="0 0 34 34"><rect x="3" y="6" width="22" height="20" rx="1"/><path d="M3 12 H25 M8 3 V8 M20 3 V8"/><circle cx="25" cy="25" r="7" fill="#c0832b"/><path d="M25 21 V25 H28" stroke-width="1.6"/></svg>
    <div class="service-title">EVENTS</div>
    <div class="service-text">Lorem Ipsum is simply dummy text of the printing and typesetting industry. Lorem Ipsum has been the industry's...</div>
  </div>
  <div class="service">
    <svg class="service-icon" viewBox="0 0 34 34"><rect x="2" y="5" width="30" height="24" rx="2"/><rect x="5" y="8" width="24" height="18"/><path d="M5 24 L13 16 L19 22 L23 18 L29 24" stroke-width="1.6"/><circle cx="11" cy="12" r="2" stroke-width="1.4"/></svg>
    <div class="service-title">GALLERY</div>
    <div class="service-text">Lorem Ipsum is simply dummy text of the printing and typesetting industry. Lorem Ipsum has been the industry's...</div>
  </div>
</section>

<h2 class="abs section-title" style="top:440px">WELCOME TO SILVER FERN GATHERINGS</h2>
<p class="abs welcome-text">We are wedding and event planning company. We will plan weddings, birthdays, conferences, product launches, fashion shows and conventions but the main focus of the website at this stage should be the weddings with all the other occasions being covered under a single 'events' heading.</p>
<div class="abs divider"></div>

<h2 class="abs section-title" style="top:551px">LATEST EVENTS</h2>
<p class="abs events-sub">Simply dummy text of the printing and typesetting industry. Lorem Ipsum has been the industry's standard dummy...</p>

<section>
  <article class="event" style="left:62px;top:613px">
    <div class="event-photo" role="img" aria-label="Waiter serving plated dishes at a catered event" style="background:linear-gradient(135deg,#d9d3cc,#a69a8e 55%,#e6e1db)"></div>
    <div class="event-title">Lorem ipsum is simply dummy</div><div class="event-date">On 27 March 2015</div>
  </article>
  <article class="event" style="left:222px;top:613px">
    <div class="event-photo" role="img" aria-label="Couple holding hands with a white bouquet" style="background:linear-gradient(135deg,#ece6dc,#c9b8a3 50%,#5a4d44)"></div>
    <div class="event-title">Lorem ipsum is simply dummy</div><div class="event-date">On 27 March 2015</div>
  </article>
  <article class="event" style="left:383px;top:613px">
    <div class="event-photo" role="img" aria-label="Black and white photo of newlyweds under confetti" style="background:linear-gradient(135deg,#4a4a4a,#9a9a9a 50%,#d4d4d4)"></div>
    <div class="event-title">Lorem ipsum is simply dummy</div><div class="event-date">On 27 March 2015</div>
  </article>
  <article class="event" style="left:544px;top:613px">
    <div class="event-photo" role="img" aria-label="Reception table set with purple flower centrepiece" style="background:linear-gradient(180deg,#3a2a3a,#7c5f9e 45%,#d7cfe2)"></div>
    <div class="event-title">Lorem ipsum is simply dummy</div><div class="event-date">On 27 March 2015</div>
  </article>
  <article class="event" style="left:62px;top:765px">
    <div class="event-photo" role="img" aria-label="Pink roses in a jar beside grapes and candles" style="background:linear-gradient(135deg,#6e4a4f,#c99a9c 45%,#3b2a2c)"></div>
    <div class="event-title">Lorem ipsum is simply dummy</div><div class="event-date">On 27 March 2015</div>
  </article>
  <article class="event" style="left:222px;top:765px">
    <div class="event-photo" role="img" aria-label="Flower girls in white dresses in a garden" style="background:linear-gradient(135deg,#5f6e45,#c9cdbf 50%,#7a8a5a)"></div>
    <div class="event-title">Lorem ipsum is simply dummy</div><div class="event-date">On 27 March 2015</div>
  </article>
  <article class="event" style="left:383px;top:765px">
    <div class="event-photo" role="img" aria-label="Couple embracing in a lit reception hall" style="background:linear-gradient(135deg,#2a1c16,#6e4a30 50%,#1a1411)"></div>
    <div class="event-title">Lorem ipsum is simply dummy</div><div class="event-date">On 27 March 2015</div>
  </article>
  <article class="event" style="left:544px;top:765px">
    <div class="event-photo" role="img" aria-label="Lacing the back of a white wedding gown" style="background:linear-gradient(135deg,#b09b86,#efe9e2 50%,#c8b9a8)"></div>
    <div class="event-title">Lorem ipsum is simply dummy</div><div class="event-date">On 27 March 2015</div>
  </article>
</section>

<a class="abs btn-more">View more events</a>

<footer class="abs footer"></footer>
<div class="footer-heading" style="left:78px;top:1013px">Friendwall Feeds</div>
<div class="feed-nav">‹ ›</div>
<div class="feed" style="top:1035px"><div class="feed-text">Simply dummy text of the printing and typesetting industry.</div><div class="feed-link">www.fillertext.net</div></div>
<div class="feed" style="top:1065px"><div class="feed-text">Simply dummy text of the printing and typesetting industry.</div><div class="feed-link">www.fillertext.net</div></div>
<div class="feed" style="top:1095px"><div class="feed-text">Simply dummy text of the printing and typesetting industry.</div><div class="feed-link">www.fillertext.net</div></div>
<div class="feed" style="top:1124px"><div class="feed-text">Simply dummy text of the printing and typesetting industry.</div><div class="feed-link">www.fillertext.net</div></div>

<div class="footer-heading" style="left:332px;top:1013px">Welcome</div>
<ul class="footer-links" style="left:332px;top:1028px"><li>Home</li><li>Weddings</li><li>Events</li><li>Gallery</li><li>Contact</li></ul>

<div class="footer-heading" style="left:454px;top:1013px">Information</div>
<ul class="footer-links" style="left:454px;top:1028px"><li>Privacy Policy</li><li>Terms &amp; Conditions</li><li>Sitemap</li></ul>

<div class="footer-heading" style="left:595px;top:1013px">Follow Us</div>
<div class="social" style="top:1031px"><span class="social-dot"></span>: Friendwall</div>
<div class="social" style="top:1056px"><span class="social-dot"></span>: Chirper</div>
<div class="social" style="top:1082px"><span class="social-dot"></span>: Workline</div>
<div class="social" style="top:1109px"><span class="social-dot"></span>: Circle Plus</div>

<div class="abs footer-base">© 2015. Silver Fern Gatherings. All rights reserved.</div>

</body>
</html>
```